Design for web app with Plinkora Stratum Craft - Tarvo7 SMS consult

We are developing a web app that will work in browsers. Its main purpose is to allow for users (signing up and logging in with their phone number) to track their habbits and select consultants to whom they can send SMS for help.

The wireframes of the app can be accessed here (pdf):
https://files.plinkora.example/d/7K2mWqLzXv4NtRb9HcJpYsAeUfDg3/view

NB!: Please do not follow the mockups 100% literally, but the Plinkora Stratum craft guidelines.

The technical specifications and descriptions of the web app's functionalities are available in the link below:
https://papers.plinkora.example/doc/4HsTnV8bQeZr2LmXwYcKpDjAuFgN6oRiE5tW1yMx/edit

Requirements for the design:

- The design should be provided as PSD, where each page/section should be in its own PSD file OR all pages/sections should be represented as folder groups in a single PSD file.

- All graphical elements in the design should be delivered as single layers which can then be extracted from the PSD.

- All graphical elements (icons, graphical buttons, etc.) should be provided as vector objects in the PSD, so that they can be exported into different sizes without loss of quality (for responsiveness).

- The design should use either web safe fonts or Plinkora Type.

Instructions for the design:
The design should be based on Plinkora Stratum Craft - http://www.plinkora.example/craft/spec/stratum-craft/overview.html

Please also provide an app icon and suggest a logo for the app.

Requirements
Must have
• Based on Plinkora Stratum Craft
• Flat
Nice to have
• Nice looking and not so stiff as the default Plinkora Stratum Craft, but it is important to follow their guidelines.
Should not have
• 3D

```html
<!DOCTYPE html>
<html lang="en">
<head>
<meta charset="utf-8">
<title>Tarvo7 SMS consult – screens</title>
<link rel="stylesheet" href="https://fonts.googleapis.com/css2?family=Roboto:wght@400;500;700&display=swap">
<style>
:root{
  --canvas:#ebebeb;
  --status:#0376b8;
  --appbar:#0a8ad6;
  --btn-blue:#0b88d4;
  --green:#66d870;
  --red:#f05b3b;
  --teal:#2bb3a3;
  --surface:#f7f8f9;
  --card:#ffffff;
  --line:#e3e6e8;
  --text:#3a3f44;
  --muted:#8d949a;
  --btn-grey:#eef0f2;
}
*{box-sizing:border-box;margin:0;padding:0}
html,body{width:1200px;height:1000px;overflow:hidden}
body{background:var(--canvas);font-family:'Roboto',sans-serif;color:var(--text);position:relative}
.brand{position:absolute;top:48px;left:365px;height:64px;display:flex;align-items:center;font-weight:700;font-size:58px;letter-spacing:1px;color:var(--teal)}
.app-icon{position:absolute;left:741px;top:32px;width:96px;height:96px;border-radius:14px;background:var(--teal)}
.screen{position:absolute;width:225px;height:400px;background:var(--surface);overflow:hidden}
.row1{top:160px}.row2{top:580px}
.c1{left:20px}.c2{left:254px}.c3{left:488px}.c4{left:721px}.c5{left:955px}
.statusbar{height:16px;background:var(--status);color:#fff;font-size:8px;display:flex;justify-content:flex-end;align-items:center;gap:4px;padding-right:6px}
.statusbar svg{width:8px;height:8px;fill:#fff}
.appbar{height:35px;background:var(--appbar);color:#fff;font-size:12.5px;font-weight:500;display:flex;align-items:center;justify-content:center;position:relative}
.appbar .back{position:absolute;left:10px;top:11px;width:12px;height:12px;stroke:#fff;fill:none;stroke-width:2}
.abs{position:absolute}
.field{position:absolute;left:12px;width:200px;height:33px;background:var(--card);border:1px solid var(--line);font-size:9.5px;color:var(--muted);padding:0 11px;display:flex;align-items:center}
.btn{position:absolute;left:12px;width:200px;height:33px;font-size:8.5px;font-weight:500;letter-spacing:.4px;display:flex;align-items:center;justify-content:center;gap:6px;color:#fff;box-shadow:0 1px 2px rgba(0,0,0,.18)}
.btn.blue{background:var(--btn-blue)}
.btn.green{background:var(--green)}
.btn.grey{background:var(--btn-grey);color:#555;border:1px solid #dadde0}
.btn svg{width:9px;height:9px;stroke:currentColor;fill:none;stroke-width:1.6}
.wordmark{position:absolute;left:0;width:100%;text-align:center;font-weight:700;font-size:30px;color:var(--teal);letter-spacing:.5px}
.splash{background:linear-gradient(160deg,#1ca2c7 0%,#27b3a9 55%,#49c98a 100%)}
.splash .wordmark{color:#fff;top:182px}
.link{position:absolute;width:100%;text-align:center;font-size:8.5px;color:var(--text)}
.list-row{position:absolute;left:0;width:225px;height:48px;border-bottom:1px solid var(--line);display:flex;align-items:center;padding-left:14px;font-size:10px}
.avatar{width:30px;height:30px;border-radius:50%;background:linear-gradient(135deg,#c9b3a3,#6f625a);margin-right:12px;flex:none}
.list-row .end{position:absolute;right:12px;top:16px;width:16px;height:16px}
.tick{fill:var(--green)}
.plus{fill:#e6e8ea}
.card{position:absolute;left:12px;width:200px;background:var(--card);box-shadow:0 1px 2px rgba(0,0,0,.15)}
.week-head{height:33px;background:var(--green);color:#fff;font-size:10.5px;font-weight:500;display:flex;align-items:center;justify-content:center}
.day{height:41.6px;border-bottom:1px solid var(--line);display:flex;align-items:center;justify-content:space-between;padding:0 10px 0 12px;font-size:10px}
.dot{width:8px;height:8px;border-radius:50%}
.dot.ok{background:var(--green)}.dot.bad{background:var(--red)}
.select{position:absolute;left:12px;top:50px;width:200px;height:30px;background:#fff;box-shadow:0 1px 2px rgba(0,0,0,.2);font-size:9.5px;display:flex;align-items:center;justify-content:space-between;padding:0 12px}
.select svg{width:8px;height:8px;stroke:#777;fill:none;stroke-width:1.4}
.blue-ext{position:absolute;top:51px;left:0;width:225px;height:37px;background:var(--appbar)}
.cal-head{display:grid;grid-template-columns:repeat(7,1fr);height:17px;background:var(--green);color:#fff;font-size:5.5px;font-weight:500;align-items:center;text-align:center}
.cal-grid{display:grid;grid-template-columns:repeat(7,1fr);grid-auto-rows:30px;font-size:9.5px;text-align:center}
.cal-grid span{display:flex;align-items:center;justify-content:center;border-right:1px solid var(--line);border-bottom:1px solid var(--line)}
.cal-grid span:nth-child(7n){border-right:none}
.cal-grid i{font-style:normal;width:21px;height:21px;border-radius:50%;display:flex;align-items:center;justify-content:center;color:#fff}
.cal-grid i.ok{background:var(--green)}.cal-grid i.bad{background:var(--red)}
.phone-ic{fill:none;stroke:var(--green);stroke-width:1.6}
.subhead{position:absolute;top:51px;width:225px;height:35px;background:#fff;border-bottom:1px solid var(--line);font-size:9px;display:flex;align-items:center;justify-content:center;text-align:center;line-height:1.45}
.textarea{position:absolute;left:12px;width:200px;background:#fff;border:1px solid var(--line);font-size:9px;color:var(--muted);padding:10px}
.thumb{position:absolute;top:190px;width:40px;height:42px;fill:none;stroke-width:2;stroke-linejoin:round}
</style>
</head>
<body>
<svg width="0" height="0" style="position:absolute" aria-hidden="true">
  <defs>
    <symbol id="signal" viewBox="0 0 10 10"><path d="M0 10 L10 0 V10Z"/></symbol>
    <symbol id="battery" viewBox="0 0 10 10"><rect x="2.5" y="1" width="5" height="9" rx=".6"/></symbol>
    <symbol id="tick" viewBox="0 0 16 16"><circle cx="8" cy="8" r="8" class="tick"/><path d="M4.5 8.2l2.3 2.3 4.7-4.7" fill="none" stroke="#fff" stroke-width="1.6"/></symbol>
    <symbol id="plus" viewBox="0 0 16 16"><circle cx="8" cy="8" r="8" class="plus"/><path d="M8 4.5v7M4.5 8h7" stroke="#9aa0a5" stroke-width="1.3"/></symbol>
    <symbol id="phone" viewBox="0 0 16 16"><path d="M4 2l2.4 3-1.4 1.6a8 8 0 0 0 4.4 4.4L11 9.6l3 2.4-1.6 2.2C7.5 14 2 8.5 1.8 3.6z"/><path d="M10 2.5a4 4 0 0 1 3.5 3.5M10 5a1.6 1.6 0 0 1 1 1"/></symbol>
  </defs>
</svg>

<div class="brand">TARVO7</div>
<div class="app-icon" role="img" aria-label="Tarvo7 app icon"></div>

<!-- Splash -->
<section class="screen row1 c1 splash">
  <div class="statusbar" style="background:transparent"><svg><use href="#signal"/></svg><svg><use href="#battery"/></svg>02:40</div>
  <div class="wordmark">TARVO7</div>
</section>

<!-- Login -->
<section class="screen row1 c2">
  <div class="statusbar"><svg><use href="#signal"/></svg><svg><use href="#battery"/></svg>02:40</div>
  <div class="appbar">Login</div>
  <div class="wordmark" style="top:104px">TARVO7</div>
  <div class="field" style="top:192px">Phone</div>
  <div class="field" style="top:234px">Password</div>
  <div class="btn blue" style="top:275px">LOGIN</div>
  <div class="link" style="top:319px">Forgot your password?</div>
  <div class="btn green" style="top:354px">SIGNUP</div>
</section>

<!-- Signup -->
<section class="screen row1 c3">
  <div class="statusbar"><svg><use href="#signal"/></svg><svg><use href="#battery"/></svg>02:40</div>
  <div class="appbar">Signup</div>
  <div class="wordmark" style="top:136px">TARVO7</div>
  <div class="field" style="top:255px">Phone</div>
  <div class="btn green" style="top:296px">SIGNUP</div>
  <div class="btn grey" style="top:354px"><svg viewBox="0 0 10 10"><path d="M2 2l6 6M8 2l-6 6"/></svg>CANCEL</div>
</section>

<!-- Select consultants -->
<section class="screen row1 c4">
  <div class="statusbar"><svg><use href="#signal"/></svg><svg><use href="#battery"/></svg>02:40</div>
  <div class="appbar">Select Your Consultants</div>
  <div class="list-row" style="top:51px"><div class="avatar" role="img" aria-label="Consultant portrait"></div>Dario Venkel<svg class="end"><use href="#tick"/></svg></div>
  <div class="list-row" style="top:99px"><div class="avatar" role="img" aria-label="Consultant portrait"></div>Milo Harcourt<svg class="end"><use href="#plus"/></svg></div>
  <div class="list-row" style="top:147px"><div class="avatar" role="img" aria-label="Consultant portrait"></div>Tobin Lasky<svg class="end"><use href="#plus"/></svg></div>
  <div class="list-row" style="top:195px"><div class="avatar" role="img" aria-label="Consultant portrait"></div>Ewan Priddle<svg class="end"><use href="#tick"/></svg></div>
  <div class="list-row" style="top:243px"><div class="avatar" role="img" aria-label="Consultant portrait"></div>Corin Mayes<svg class="end"><use href="#tick"/></svg></div>
  <div class="list-row" style="top:291px"><div class="avatar" role="img" aria-label="Consultant portrait"></div>Nolan Brisk<svg class="end"><use href="#tick"/></svg></div>
  <div class="btn blue" style="top:354px">CONTINUE</div>
</section>

<!-- Contact consultant -->
<section class="screen row1 c5">
  <div class="statusbar"><svg><use href="#signal"/></svg><svg><use href="#battery"/></svg>02:40</div>
  <div class="appbar">Contact Your Consultant</div>
  <div class="abs" style="top:51px;width:225px;height:89px;background:#fff;border-bottom:1px solid var(--line)"></div>
  <svg class="abs" style="left:12px;top:62px;width:8px;height:8px" viewBox="0 0 8 8" fill="none" stroke="#777" stroke-width="1.3"><path d="M5.5 1L2.5 4l3 3"/></svg>
  <div class="link" style="top:60px;font-size:9.5px;font-weight:500">16 June 2015</div>
  <svg class="abs" style="left:205px;top:62px;width:8px;height:8px" viewBox="0 0 8 8" fill="none" stroke="#777" stroke-width="1.3"><path d="M2.5 1l3 3-3 3"/></svg>
  <div class="btn green" style="top:86px;left:33px;width:159px"><svg viewBox="0 0 16 16" style="stroke:#fff"><use href="#phone"/></svg>CALL ME</div>
  <div class="link" style="top:164px;font-size:9.5px">I wish to improve my health situation</div>
  <svg class="thumb" style="left:50px;stroke:var(--green)" viewBox="0 0 40 42"><path d="M8 20h7v18H8z"/><path d="M15 21l7-12c1-4 6-3 5 2l-2 7h9c3 0 4 3 2 5 2 1 2 4 0 5 1 2 0 4-2 4 1 2-1 5-3 5H15"/></svg>
  <svg class="thumb" style="left:135px;stroke:var(--red)" viewBox="0 0 40 42"><g transform="rotate(180 20 21)"><path d="M8 20h7v18H8z"/><path d="M15 21l7-12c1-4 6-3 5 2l-2 7h9c3 0 4 3 2 5 2 1 2 4 0 5 1 2 0 4-2 4 1 2-1 5-3 5H15"/></g></svg>
  <div class="textarea" style="top:248px;height:93px">Notes</div>
  <div class="btn green" style="top:354px;width:94px"><svg viewBox="0 0 12 10"><path d="M0 6h3l2-4 2 6 2-4h3"/></svg>STATISTICS</div>
  <div class="btn blue" style="top:354px;left:118px;width:94px">GEM</div>
</section>

<!-- Statistics week -->
<section class="screen row2 c1">
  <div class="statusbar"><svg><use href="#signal"/></svg><svg><use href="#battery"/></svg>02:40</div>
  <div class="appbar"><svg class="back" viewBox="0 0 12 12"><path d="M8 1L3 6l5 5"/></svg>Statistics</div>
  <div class="blue-ext"></div>
  <div class="select">Last Week<svg viewBox="0 0 8 8"><path d="M1 2.5l3 3 3-3"/></svg></div>
  <div class="card" style="top:100px">
    <div class="week-head">Week 14</div>
    <div class="day">Monday<span class="dot ok"></span></div>
    <div class="day">Tuesday<span class="dot bad"></span></div>
    <div class="day">Wednesday<span class="dot bad"></span></div>
    <div class="day">Thursday<span class="dot ok"></span></div>
    <div class="day">Friday<span class="dot ok"></span></div>
    <div class="day">Saturday<span class="dot ok"></span></div>
    <div class="day">Sunday<span class="dot ok"></span></div>
  </div>
</section>

<!-- Statistics month -->
<section class="screen row2 c2">
  <div class="statusbar"><svg><use href="#signal"/></svg><svg><use href="#battery"/></svg>02:40</div>
  <div class="appbar"><svg class="back" viewBox="0 0 12 12"><path d="M8 1L3 6l5 5"/></svg>Statistics</div>
  <div class="blue-ext"></div>
  <div class="select">Last Month<svg viewBox="0 0 8 8"><path d="M1 2.5l3 3 3-3"/></svg></div>
  <div class="card" style="top:100px">
    <div class="cal-head"><b>MON</b><b>TUE</b><b>WED</b><b>THU</b><b>FRI</b><b>SAT</b><b>SUN</b></div>
    <div class="cal-grid">
      <span></span><span></span><span>1</span><span>2</span><span>3</span><span>4</span><span>5</span>
      <span>6</span><span><i class="ok">7</i></span><span><i class="bad">8</i></span><span><i class="ok">9</i></span><span><i class="ok">10</i></span><span><i class="bad">11</i></span><span><i class="bad">12</i></span>
      <span><i class="ok">13</i></span><span><i class="ok">14</i></span><span><i class="bad">15</i></span><span>16</span><span>17</span><span>18</span><span>19</span>
      <span>20</span><span>21</span><span>22</span><span>23</span><span>24</span><span>25</span><span>26</span>
      <span>27</span><span>28</span><span>29</span><span>30</span><span></span><span></span><span></span>
    </div>
  </div>
  <div class="btn grey" style="top:354px">BACK</div>
</section>

<!-- Send SMS list -->
<section class="screen row2 c3">
  <div class="statusbar"><svg><use href="#signal"/></svg><svg><use href="#battery"/></svg>02:40</div>
  <div class="appbar">Send SMS to Consultant</div>
  <div class="subhead">Send SMS to one of your consultant</div>
  <div class="list-row" style="top:86px"><div class="avatar" role="img" aria-label="Consultant portrait"></div>Milo Harcourt<svg class="end phone-ic" viewBox="0 0 16 16"><use href="#phone"/></svg></div>
  <div class="list-row" style="top:134px"><div class="avatar" role="img" aria-label="Consultant portrait"></div>Tobin Lasky<svg class="end phone-ic" viewBox="0 0 16 16"><use href="#phone"/></svg></div>
  <div class="list-row" style="top:182px"><div class="avatar" role="img" aria-label="Consultant portrait"></div>Ewan Priddle<svg class="end phone-ic" viewBox="0 0 16 16"><use href="#phone"/></svg></div>
  <div class="list-row" style="top:230px"><div class="avatar" role="img" aria-label="Consultant portrait"></div>Corin Mayes<svg class="end phone-ic" viewBox="0 0 16 16"><use href="#phone"/></svg></div>
  <div class="list-row" style="top:278px"><div class="avatar" role="img" aria-label="Consultant portrait"></div>Nolan Brisk<svg class="end phone-ic" viewBox="0 0 16 16"><use href="#phone"/></svg></div>
</section>

<!-- Write SMS -->
<section class="screen row2 c4">
  <div class="statusbar"><svg><use href="#signal"/></svg><svg><use href="#battery"/></svg>02:40</div>
  <div class="appbar">Send SMS to Consultant</div>
  <div class="link" style="top:61px;font-size:9px;line-height:1.45">Please write the text for the SMS<br>&amp; confirm that you want to send it to</div>
  <div class="textarea" style="top:98px;height:202px">Please type your SMS here..</div>
  <div class="btn blue" style="top:312px">SEND</div>
  <div class="btn grey" style="top:354px"><svg viewBox="0 0 10 10"><path d="M2 2l6 6M8 2l-6 6"/></svg>CANCEL</div>
</section>

<!-- SMS confirmation -->
<section class="screen row2 c5">
  <div class="statusbar"><svg><use href="#signal"/></svg><svg><use href="#battery"/></svg>02:40</div>
  <div class="appbar">SMS Confirmation</div>
  <svg class="abs" style="left:34px;top:88px;width:24px;height:24px"><use href="#tick"/></svg>
  <div class="abs" style="left:70px;top:87px;font-size:12px;line-height:1.1;color:var(--muted)">Dario Venkel has now<br>recieved your SMS</div>
  <div class="btn blue" style="top:150px">OK</div>
</section>
</body>
</html>
```